Aircraft maintenance buisness card

I am an aircraft mechanic looking for a personal buisness card . I would like my name and a title of Aircraft Maintenance Manager . I would like a suttle picture of an aircraft and helicopter .

elegant and professional wtih my contact .

My name should be on the car and Aircraft Maintenance Manager under with my contact infor below .

i have attached some pictures but i am open to other pics and ideas . I would like a airliner or private jet and a helicopter in the picture . The Images should be suttle and not the main idea . I also uploaded a picture of a jet engine which is cool . Be creative and i will work with you to finalize something .
Updates

Project Deadline Extended
Reason: Looking for more variations . Very good so far but looiking for a bit more styles and i uploaded my logo that i purchased . Please use my logo and be creative with it . I like some variations of black card with maybe some pictures that i uploaded but i am open to ideas . Be creative and i will work with you .

Project Deadline Extended
Reason: Looking for more designs and variations . Not yet satisfied with the designs i have gotten .

Industry/Entity Type

Aviation

Contact Information for Business Card

Aircraft Maintenance Manager

Font styles to use
Serif

Colors

Designer to choose colors to be used in the design.

Requirements
Must have
• An aviation related Logo if possible incorporated in the card possibly
• My name
• Tobias Marven Ellery
• 482 Pellow Ave.
• Brelton , NK
• 07519
• Email: Tmskyworks@quillmail.net
Nice to have
• Suttle Backround of a Private Jet or Airliner and a Helicopter .

```html
<!DOCTYPE html>
<html lang="en">
<head>
<meta charset="utf-8">
<title>Marven Aviation – Business Card</title>
<link rel="stylesheet" href="https://fonts.googleapis.com/css2?family=Montserrat:ital,wght@0,400;0,700;1,400&display=swap">
<style>
  :root {
    --stage: #e4e4e4;
    --card: #ffffff;
    --brand-blue: #1a47a0;
    --ink-grey: #6d6e71;
    --rule-blue: #3a63b8;
  }
  * { margin: 0; padding: 0; box-sizing: border-box; }
  html, body { width: 1200px; height: 798px; overflow: hidden; }
  body {
    background: var(--stage);
    font-family: "Montserrat", Arial, sans-serif;
    position: relative;
  }
  .card {
    position: absolute;
    left: 395px;
    width: 522px;
    height: 298px;
    background: var(--card);
    overflow: hidden;
  }
  .card--front { top: 83px; }
  .card--back { top: 447px; }

  .brand {
    position: absolute;
    display: flex;
    align-items: center;
    gap: 12px;
  }
  .brand__square {
    background: var(--brand-blue);
    border-radius: 10px;
  }
  .brand__name {
    color: var(--brand-blue);
    font-weight: 700;
    letter-spacing: 0.06em;
    white-space: nowrap;
  }
  .card--front .brand { left: 0; right: 0; top: 120px; justify-content: center; }
  .card--front .brand__square { width: 92px; height: 92px; }
  .card--front .brand__name { font-size: 26px; }

  .card--back .brand { right: 16px; top: 32px; gap: 8px; }
  .card--back .brand__square { width: 54px; height: 54px; border-radius: 7px; }
  .card--back .brand__name { font-size: 15px; }

  .card__art { position: absolute; left: 0; top: 0; width: 522px; height: 298px; }

  .contact {
    position: absolute;
    right: 16px;
    top: 168px;
    text-align: right;
  }
  .contact__name {
    color: var(--brand-blue);
    font-weight: 700;
    font-size: 14.5px;
    letter-spacing: 0.01em;
    text-transform: uppercase;
  }
  .contact__title {
    color: var(--ink-grey);
    font-style: italic;
    font-size: 8.6px;
    text-transform: uppercase;
    margin-top: 2px;
  }
  .contact__rule {
    width: 236px;
    height: 1px;
    background: var(--rule-blue);
    margin: 6px 0 12px auto;
  }
  .contact__line {
    color: var(--ink-grey);
    font-size: 11px;
    line-height: 13px;
  }
</style>
</head>
<body>

<section class="card card--front">
  <div class="brand">
    <span class="brand__square"></span>
    <span class="brand__name">MARVEN AVIATION</span>
  </div>
</section>

<section class="card card--back">
  <svg class="card__art" viewBox="0 0 522 298">
    <defs>
      <linearGradient id="jetGrad" x1="0" y1="0" x2="0" y2="1">
        <stop offset="0" stop-color="#3d5c94"/>
        <stop offset="1" stop-color="#1e2e50"/>
      </linearGradient>
      <linearGradient id="heliGrad" x1="0" y1="0" x2="1" y2="1">
        <stop offset="0" stop-color="#8c8478"/>
        <stop offset="1" stop-color="#5e564c"/>
      </linearGradient>
      <linearGradient id="linerGrad" x1="0" y1="0" x2="0" y2="1">
        <stop offset="0" stop-color="#a8b8c8"/>
        <stop offset="1" stop-color="#5f7a8c"/>
      </linearGradient>
    </defs>
    <g role="img" aria-label="Private jet parked on the ramp at dusk">
      <rect x="8" y="6" width="120" height="74" fill="url(#jetGrad)"/>
    </g>
    <g role="img" aria-label="Blue and white helicopter flying past a rocky cliff">
      <rect x="8" y="85" width="160" height="97" fill="url(#heliGrad)"/>
    </g>
    <g role="img" aria-label="Wide-body airliner flying above the coastline">
      <rect x="8" y="186" width="220" height="104" fill="url(#linerGrad)"/>
    </g>
    <polygon points="35,0 107,0 281,298 214,298" fill="var(--brand-blue)"/>
    <polygon points="107,0 522,0 522,298 281,298" fill="var(--card)"/>
    <line x1="121" y1="0" x2="293" y2="298" stroke="var(--rule-blue)" stroke-width="0.8"/>
  </svg>

  <div class="brand">
    <span class="brand__square"></span>
    <span class="brand__name">MARVEN AVIATION</span>
  </div>

  <div class="contact">
    <p class="contact__name">Tobias Marven Ellery</p>
    <p class="contact__title">Aircraft Maintenance Manager</p>
    <div class="contact__rule"></div>
    <p class="contact__line">tmskyworks@quillmail.net</p>
    <p class="contact__line">482 Pellow Ave. ,Brelton , NK&nbsp; 07519</p>
  </div>
</section>

</body>
</html>
```